innovative investment real estate sales firm

We are a uniquely collabrative firm that seeks to bring a conultative approach to uncovering hidden opportunities for our clients, our website needs to convey our client focused approach. Our firm specializes in the sale of apartment properties in Southern California. We have a team of researchers, transaction coordinators and marketing personal to support our geographically specialized advisers. We need a website that introduces clients to our unique way of better helping them achieve their investment goals.

Target Market(s)

High net worth individuals and families

Industry/Entity Type

Real Estate Agent

Font styles to use
Other font styles liked:
• please use font provided

Requirements
Must have
• Stories of our recent projects
• Features on our people
• email capture for viewing inventory
• content that showcases our unique consultative approach that uncovers unrealized opportunities

```html
<!DOCTYPE html>
<html lang="en">
<head>
<meta charset="utf-8">
<title>Meridian Advisers – Multifamily Properties</title>
<link rel="stylesheet" href="https://fonts.googleapis.com/css2?family=Nunito+Sans:wght@300;400;600;700&family=Lato:wght@400;700&display=swap">
<style>
  :root {
    --teal: #0aa0b9;
    --teal-dark: #078aa0;
    --ink: #222222;
    --body: #555555;
    --green: #8cc63f;
    --btn-green: #1d7a4a;
    --grey-bg: #ececec;
    --white: #ffffff;
    --black: #0a0a0a;
  }
  * { box-sizing: border-box; margin: 0; padding: 0; }
  html, body { width: 739px; height: 1200px; overflow: hidden; background: var(--white); }
  body { position: relative; font-family: "Lato", sans-serif; color: var(--ink); }

  .site-header { position: absolute; top: 0; left: 0; width: 739px; height: 64px; background: var(--white); z-index: 2; box-shadow: 0 4px 10px rgba(0,0,0,.12); }
  .brand { position: absolute; left: 48px; top: 22px; display: flex; align-items: center; gap: 8px; font-family: "Nunito Sans", sans-serif; font-weight: 700; font-size: 15px; letter-spacing: 2px; color: var(--teal-dark); }
  .brand-mark { width: 14px; height: 14px; background: var(--teal); }
  .main-nav { position: absolute; top: 20px; left: 351px; display: flex; align-items: center; font-family: "Nunito Sans", sans-serif; font-size: 10.5px; }
  .main-nav a { color: var(--ink); text-decoration: none; padding: 5px 10px; margin-right: 16px; border-radius: 2px; }
  .main-nav a.is-active { background: var(--teal); color: var(--white); font-weight: 600; }
  .nav-divider { position: absolute; left: 650px; top: 20px; width: 1px; height: 24px; background: #ddd; }
  .search-icon { position: absolute; left: 662px; top: 24px; }

  .hero { position: absolute; top: 64px; left: 0; width: 739px; height: 352px;
    background:
      linear-gradient(180deg, rgba(0,0,0,0) 78%, #5c5a58 88%, #3e3c3b 100%),
      linear-gradient(90deg, rgba(60,80,60,.55) 0%, rgba(0,0,0,0) 22%, rgba(0,0,0,0) 78%, rgba(50,70,50,.5) 100%),
      linear-gradient(180deg, rgba(0,0,0,0) 18%, rgba(232,226,224,.9) 30%, rgba(214,206,204,.95) 62%, rgba(160,120,90,.8) 78%, rgba(0,0,0,0) 80%),
      linear-gradient(180deg, #7e97d3 0%, #a5b4dc 40%, #c2c8df 100%); }
  .hero-thumbs { position: absolute; top: 387px; left: 276px; display: flex; gap: 6px; z-index: 1; }
  .hero-thumb { width: 58px; height: 58px; border-radius: 50%; border: 3px solid var(--white); box-shadow: 0 2px 4px rgba(0,0,0,.2); }
  .thumb-one { background: linear-gradient(135deg, #d8cfc4, #a0724a 50%, #3d3a38); }
  .thumb-two { background: linear-gradient(135deg, #7fd0dd, #2a95ac 50%, #155e72); }
  .thumb-three { background: linear-gradient(180deg, #7fa862 0%, #e8e2da 40%, #c18772 100%); }

  .section-title { position: absolute; left: 0; width: 739px; text-align: center; font-family: "Nunito Sans", sans-serif; font-weight: 400; font-size: 26px; color: var(--ink); }
  .section-title span { color: var(--teal); }
  .divider { position: absolute; left: 50%; transform: translateX(-50%); width: 280px; height: 8px; }
  .intro-text { position: absolute; top: 534px; left: 90px; width: 559px; text-align: center; font-size: 10.4px; line-height: 17px; color: var(--body); }
  .btn-learn { position: absolute; top: 579px; left: 295px; width: 149px; height: 36px; border: 1.5px solid var(--btn-green); color: var(--btn-green); font-size: 11px; display: flex; align-items: center; justify-content: center; gap: 5px; text-decoration: none; }

  .projects { position: absolute; top: 646px; left: 0; width: 739px; height: 432px; background: var(--grey-bg); }
  .filters { position: absolute; top: 86px; left: 266px; display: flex; gap: 16px; font-family: "Nunito Sans", sans-serif; font-size: 11.5px; color: #555; align-items: center; }
  .filters .filter { padding: 6px 0; }
  .filters .is-active { background: var(--black); color: var(--white); width: 52px; text-align: center; border-radius: 3px; }
  .tile { position: absolute; }
  .tile-a { left: 48px; top: 132px; width: 205px; height: 115px;
    background: linear-gradient(180deg, rgba(0,0,0,0) 55%, rgba(70,80,95,.85) 100%), linear-gradient(90deg, #6f6d6c 0%, #8a8886 35%, #3f79c9 45%, #3d7ad0 62%, #dfe3e8 72%, #8a949e 100%); }
  .tile-b { left: 48px; top: 256px; width: 205px; height: 115px;
    background: linear-gradient(180deg, rgba(0,0,0,0) 45%, #d7e0ea 60%, #b9c7d6 100%), linear-gradient(90deg, #c9d8e6 0%, #b7a99a 45%, #a35a3a 70%, #e8e4de 100%); }
  .tile-c { left: 486px; top: 132px; width: 206px; height: 115px;
    background: linear-gradient(180deg, #4a5d8c 0%, #c07f7a 28%, #8b7b86 45%, #d9cfc0 62%, #6a5140 82%, #3a4a3a 100%); }
  .tile-d { left: 486px; top: 256px; width: 206px; height: 115px;
    background: linear-gradient(90deg, rgba(0,0,0,0) 30%, rgba(235,238,240,.9) 40%, rgba(20,140,155,.85) 55%, rgba(235,238,240,.9) 70%, rgba(0,0,0,0) 80%), linear-gradient(180deg, #3d6fc4 0%, #8fa8d4 60%, #6d9a6a 100%); }
  .tile-feature { left: 267px; top: 132px; width: 206px; height: 239px;
    background: linear-gradient(180deg, rgba(0,0,0,0) 45%, rgba(10,12,18,.95) 100%), linear-gradient(100deg, #2d4f86 0%, #5c86b8 30%, #203552 55%, #a05a3a 72%, #3a5f8c 100%); }
  .feature-frame { position: absolute; left: 7px; top: 7px; right: 7px; bottom: 7px; border: 1px solid rgba(255,255,255,.55); }
  .feature-name { position: absolute; top: 160px; width: 100%; text-align: center; color: var(--white); font-family: "Nunito Sans", sans-serif; font-weight: 600; font-size: 19px; letter-spacing: 3px; }
  .feature-text { position: absolute; top: 194px; left: 16px; right: 16px; text-align: center; color: var(--white); font-size: 8.6px; line-height: 13px; }

  .site-footer { position: absolute; top: 1078px; left: 0; width: 739px; height: 122px; background: var(--teal); color: var(--white); }
  .footer-badge { position: absolute; top: 1046px; left: 338px; width: 64px; height: 64px; border-radius: 50%; background: var(--white); border: 2px solid #d7d7d7; z-index: 1; display: flex; align-items: center; justify-content: center; }
  .footer-badge span { width: 16px; height: 16px; background: var(--teal); }
  .footer-nav { position: absolute; top: 20px; left: 49px; display: flex; gap: 21px; font-size: 9px; }
  .social { position: absolute; top: 14px; left: 602px; display: flex; gap: 6px; }
  .social span { width: 26px; height: 26px; border: 1px solid var(--white); }
  .social span:first-child { background: var(--white); }
  .footer-rule { position: absolute; top: 48px; left: 49px; width: 643px; height: 1px; background: rgba(255,255,255,.6); }
  .footer-contact { position: absolute; top: 68px; font-size: 9px; line-height: 13px; display: flex; gap: 7px; align-items: flex-start; }
  .address { left: 49px; }
  .phone { left: 358px; top: 74px; align-items: center; }
  .email { left: 534px; top: 74px; align-items: center; }
  .copyright { position: absolute; top: 104px; width: 100%; text-align: center; font-size: 7px; }
  .copyright strong { font-family: "Nunito Sans", sans-serif; font-size: 12px; font-weight: 600; }
</style>
</head>
<body>
  <header class="site-header">
    <div class="brand"><span class="brand-mark"></span>MERIDIAN ADVISERS</div>
    <nav class="main-nav">
      <a href="#" class="is-active">Home</a>
      <a href="#">About</a>
      <a href="#">Recent Projects</a>
      <a href="#">Contact</a>
    </nav>
    <div class="nav-divider"></div>
    <svg class="search-icon" width="16" height="16" viewBox="0 0 16 16"><circle cx="6.5" cy="6.5" r="5" fill="none" stroke="#0aa0b9" stroke-width="2.2"/><line x1="10" y1="10" x2="14.5" y2="14.5" stroke="#0aa0b9" stroke-width="2.6" stroke-linecap="round"/></svg>
  </header>

  <section class="hero" role="img" aria-label="Modern multifamily apartment complex with palm trees at dusk"></section>
  <div class="hero-thumbs">
    <div class="hero-thumb thumb-one" role="img" aria-label="Apartment tower exterior"></div>
    <div class="hero-thumb thumb-two" role="img" aria-label="Teal-tinted residential building"></div>
    <div class="hero-thumb thumb-three" role="img" aria-label="Outdoor patio with fire pit"></div>
  </div>

  <h1 class="section-title" style="top:476px;">Welcome to <span>MERIDIAN ADVISERS</span></h1>
  <svg class="divider" style="top:514px;" viewBox="0 0 280 8"><defs><linearGradient id="lineFade" x1="0" x2="1"><stop offset="0" stop-color="#0aa0b9" stop-opacity="0"/><stop offset=".5" stop-color="#0aa0b9"/><stop offset="1" stop-color="#0aa0b9" stop-opacity="0"/></linearGradient></defs><rect x="0" y="3.5" width="280" height="1" fill="url(#lineFade)"/><rect x="137.2" y="1.2" width="5.6" height="5.6" fill="#8cc63f" transform="rotate(45 140 4)"/></svg>
  <p class="intro-text">Lorem Ipsum is simply dummy text of the printing and typesetting industry. Lorem Ipsum has been the industry's standard dummy text ever since the 1500s, when an unknown printer took a galley of type and scrambled it.</p>
  <a href="#" class="btn-learn">Learn More About Us <svg width="6" height="8" viewBox="0 0 6 8"><path d="M0 0 L6 4 L0 8 Z" fill="#1d7a4a"/></svg></a>

  <section class="projects">
    <h2 class="section-title" style="top:30px;">Recent <span>PROJECTS</span></h2>
    <svg class="divider" style="top:68px;" viewBox="0 0 280 8"><rect x="0" y="3.5" width="280" height="1" fill="url(#lineFade)"/><rect x="137.2" y="1.2" width="5.6" height="5.6" fill="#8cc63f" transform="rotate(45 140 4)"/></svg>
    <div class="filters">
      <span class="filter is-active">All</span>
      <span class="filter">Commercial</span>
      <span class="filter">Residential</span>
    </div>
    <div class="tile tile-a" role="img" aria-label="Modern apartment buildings with balconies under blue sky"></div>
    <div class="tile tile-b" role="img" aria-label="Rooftop lounge with orange chairs and city skyline"></div>
    <div class="tile tile-feature" role="img" aria-label="Glass office tower at dusk">
      <div class="feature-frame"></div>
      <div class="feature-name">MERIDIAN</div>
      <p class="feature-text">Lorem Ipsum is simply dummy text of the printing and typesetting industry.</p>
    </div>
    <div class="tile tile-c" role="img" aria-label="Residential entrance canopy at sunset"></div>
    <div class="tile tile-d" role="img" aria-label="White and teal apartment tower"></div>
  </section>

  <div class="footer-badge"><span></span></div>
  <footer class="site-footer">
    <nav class="footer-nav"><span>Home</span><span>About</span><span>Recent Project</span><span>Contact Us</span></nav>
    <div class="social" aria-label="Social links"><span></span><span></span><span></span></div>
    <div class="footer-rule"></div>
    <div class="footer-contact address">
      <svg width="14" height="16" viewBox="0 0 14 16"><path d="M7 1C4 1 2 3.2 2 6c0 3.5 5 9 5 9s5-5.5 5-9c0-2.8-2-5-5-5z" fill="#fff"/><circle cx="7" cy="6" r="1.8" fill="#0aa0b9"/></svg>
      <div>MERIDIAN ADVISERS<br>123 Building Name, City, Country - zipcode</div>
    </div>
    <div class="footer-contact phone">
      <svg width="14" height="14" viewBox="0 0 14 14"><path d="M3 1l2.5 3-1.5 1.5c.8 1.8 2.2 3.2 4 4L9.5 8 12.5 10.5 11 13C6 12.5 1.5 8 1 3z" fill="none" stroke="#fff" stroke-width="1"/></svg>
      <span>+44 (0) 7000 315264</span>
    </div>
    <div class="footer-contact email">
      <svg width="16" height="12" viewBox="0 0 16 12"><rect x=".6" y=".6" width="14.8" height="10.8" fill="none" stroke="#fff" stroke-width="1.2"/><path d="M1 1 L8 7 L15 1" fill="none" stroke="#fff" stroke-width="1.2"/></svg>
      <span>hello@meridianadv.com</span>
    </div>
    <p class="copyright">© <strong>Meridian Advisers</strong> - 2017 All Right Reserved</p>
  </footer>
</body>
</html>
```